House Builder and Property Development Card Design and Logo

I need a business card design for a building and property development company.
Colour scheme of Dark Grey and Green, I would like it bold, sharp and professional.
No logo yet done, I'm open to options but please stay away from the usual- house, roof, hammers etc.
Thanks Rob

Please be aware that on the business card information section the WHRC # 5528391 is a licence number and my phone number 0492837165. The numbers are close together and could be mistaken as one whole number 

Thank you

                                   

Industry/Entity Type

Building

Contact Information for Business Card

VARGA BUILD & DEVELOPMENT.
Residential Building & Property Development
Robert Varga - Director
WHRC # 5528391
0492837165
rob@vargabuild.example.com.au

Requirements
Must have
• Bold Business name
Dark grey and green colours
Should not have
• roof outline or hammer logo

```html
<!DOCTYPE html>
<html lang="en">
<head>
<meta charset="utf-8">
<title>Varga Build &amp; Development – Business Card</title>
<link rel="stylesheet" href="https://fonts.googleapis.com/css2?family=Cormorant+Garamond:wght@600&family=Open+Sans:wght@400;600&display=swap">
<style>
  :root {
    --backdrop: #d9d3cd;
    --charcoal: #2b2b2d;
    --charcoal-deep: #232325;
    --green: #08b35a;
    --green-mid: #05a251;
    --green-dark: #068f47;
    --white: #ffffff;
    --grey-text: #c9c9c9;
  }
  * { box-sizing: border-box; margin: 0; padding: 0; }
  html, body {
    width: 1200px; height: 901px; overflow: hidden;
    background: var(--backdrop);
  }
  .sheet {
    position: relative; width: 1200px; height: 901px;
    display: flex; align-items: center; justify-content: center; gap: 60px;
  }
  .card {
    position: relative; width: 525px; height: 300px;
    border-radius: 22px; overflow: hidden;
    box-shadow: 0 10px 24px rgba(0,0,0,.22);
  }
  .card--front { background: var(--charcoal); }
  .card--back { background: var(--green); }
  .card__wave { position: absolute; inset: 0; width: 100%; height: 100%; }

  .brand {
    position: absolute; left: 0; right: 0;
    display: flex; flex-direction: column; align-items: center;
  }
  .card--front .brand { top: 108px; }
  .card--back .brand { top: 62px; left: -70px; }
  .brand__row { display: flex; align-items: center; gap: 10px; }
  .brand__dot {
    width: 14px; height: 14px; border-radius: 50%; background: var(--green);
  }
  .card--back .brand__dot { background: var(--white); }
  .brand__name {
    font-family: "Cormorant Garamond", "Times New Roman", serif;
    font-weight: 600; font-size: 27px; letter-spacing: .5px;
    color: var(--white); white-space: nowrap;
  }
  .brand__rule {
    width: 300px; height: 1px; margin-top: 4px;
    background: var(--green);
  }
  .card--back .brand__rule { background: var(--white); }
  .brand__tagline {
    margin-top: 4px;
    font-family: "Open Sans", Arial, sans-serif; font-size: 8.5px;
    letter-spacing: 1.6px; color: var(--white); text-transform: uppercase;
  }

  .contact {
    position: absolute; right: 28px; top: 150px; text-align: right;
    color: var(--white);
  }
  .contact__name {
    font-family: "Cormorant Garamond", "Times New Roman", serif;
    font-weight: 600; font-size: 25px; line-height: 1;
  }
  .contact__role {
    font-family: "Open Sans", Arial, sans-serif; font-size: 9px;
    letter-spacing: 2px; color: var(--grey-text); margin-top: 2px;
  }
  .contact__lines {
    margin-top: 18px;
    font-family: "Open Sans", Arial, sans-serif; font-size: 11.5px;
    color: var(--grey-text); line-height: 1.8;
  }
  .contact__line { display: flex; justify-content: flex-end; align-items: center; gap: 6px; }
  .contact__licence { margin-right: 14px; }
  .icon { width: 11px; height: 11px; fill: var(--green); }
</style>
</head>
<body>
<main class="sheet">
  <section class="card card--front" aria-label="Card front">
    <div class="brand">
      <div class="brand__row">
        <span class="brand__dot"></span>
        <span class="brand__name">VARGA BUILD &amp; DEVELOPMENT</span>
      </div>
      <div class="brand__rule"></div>
      <p class="brand__tagline">Residential Building and Property Development</p>
    </div>
  </section>

  <section class="card card--back" aria-label="Card back">
    <svg class="card__wave" viewBox="0 0 525 300" preserveAspectRatio="none" aria-hidden="true">
      <path fill="var(--green-dark)" d="M0 240 C120 252 200 205 270 145 C340 85 420 75 525 70 L525 300 L0 300Z"/>
      <path fill="var(--green-mid)" d="M0 252 C120 262 205 218 275 158 C345 98 425 88 525 84 L525 300 L0 300Z"/>
      <path fill="var(--charcoal)" d="M0 264 C125 272 210 230 280 170 C350 110 430 100 525 98 L525 300 L0 300Z"/>
    </svg>
    <div class="brand">
      <div class="brand__row">
        <span class="brand__dot"></span>
        <span class="brand__name">VARGA BUILD &amp; DEVELOPMENT</span>
      </div>
      <div class="brand__rule"></div>
      <p class="brand__tagline">Residential Building and Property Development</p>
    </div>
    <div class="contact">
      <p class="contact__name">Robert Varga</p>
      <p class="contact__role">DIRECTOR</p>
      <div class="contact__lines">
        <p class="contact__line">
          <span class="contact__licence">WHRC#5528391</span>
          <svg class="icon" viewBox="0 0 24 24" aria-hidden="true"><path d="M6.6 10.8a15.1 15.1 0 0 0 6.6 6.6l2.2-2.2a1 1 0 0 1 1-.25 11.4 11.4 0 0 0 3.6.57 1 1 0 0 1 1 1V20a1 1 0 0 1-1 1A17 17 0 0 1 3 4a1 1 0 0 1 1-1h3.5a1 1 0 0 1 1 1c0 1.25.2 2.45.57 3.57a1 1 0 0 1-.25 1z"/></svg>
          <span>04 92 837 165</span>
        </p>
        <p class="contact__line">
          <svg class="icon" viewBox="0 0 24 24" aria-hidden="true"><path d="M2 5h20v14H2z M2 5l10 8 10-8" /></svg>
          <span>rob@vargabuild.example.com.au</span>
        </p>
      </div>
    </div>
  </section>
</main>
</body>
</html>
```